Business Card Design Project

See the detainl of the Vortel company project I also have live: http://tasks.quillmarsh.com/task.aspx?id=382917

Reason: I am waiting to select a logo design and ideally the business card design will be from the same person

Industry/Entity Type

Business

```html
<!DOCTYPE html>
<html lang="en">
<head>
<meta charset="utf-8">
<title>Halvern LLP – Business Card</title>
<link rel="stylesheet" href="https://fonts.googleapis.com/css2?family=PT+Sans:wght@400&family=Quicksand:wght@700&display=swap">
<style>
  :root {
    --navy: #1f3a8c;
    --sky: #1ba3e1;
    --paper: #ffffff;
  }
  html, body {
    margin: 0;
    padding: 0;
    width: 1200px;
    height: 805px;
    overflow: hidden;
    background: var(--paper);
  }
  .card {
    position: relative;
    width: 1200px;
    height: 805px;
    background: var(--paper);
    color: var(--navy);
  }
  .brand {
    position: absolute;
    left: 90px;
    top: 150px;
    display: flex;
    align-items: center;
    gap: 16px;
  }
  .brand-dot {
    width: 34px;
    height: 34px;
    border-radius: 50%;
    background: var(--sky);
  }
  .brand-name {
    font-family: "Quicksand", sans-serif;
    font-weight: 700;
    font-size: 44px;
    color: var(--navy);
    letter-spacing: 1px;
    line-height: 1;
  }
  .person-name {
    position: absolute;
    right: 97px;
    top: 157px;
    margin: 0;
    font-family: "PT Sans", sans-serif;
    font-weight: 400;
    font-size: 52px;
    line-height: 1;
    color: var(--navy);
  }
  .contact {
    position: absolute;
    right: 97px;
    text-align: right;
    font-family: "Quicksand", sans-serif;
    font-weight: 700;
    font-size: 24px;
    line-height: 34.3px;
    letter-spacing: 1.2px;
    word-spacing: 4px;
    color: var(--navy);
    margin: 0;
    font-style: normal;
  }
  .address { top: 344px; }
  .details { top: 544px; }
  .contact span { display: block; white-space: nowrap; }
</style>
</head>
<body>
  <main class="card">
    <div class="brand">
      <span class="brand-dot"></span>
      <span class="brand-name">Halvern LLP</span>
    </div>

    <h1 class="person-name">Tom Ashby</h1>

    <address class="contact address">
      <span>Meridian Works</span>
      <span>41 Fenbrook Business Park</span>
      <span>Carlow Road</span>
      <span>Ellisford</span>
      <span>EF7 2QT</span>
    </address>

    <p class="contact details">
      <span>Email: tom.ashby@halvern.co.uk</span>
      <span>Web: www.halvern.co.uk</span>
      <span>Tel +44 (0)1632 960481</span>
      <span>Fax: (0)1632 960482</span>
      <span>Mobile: +44 (0)7700 900XXX</span>
    </p>
  </main>
</body>
</html>
```